Creative, Colorful, Dynamic Infographic for Global Non-Profit

We are a global arts and education non-profit in need of an infographic that illustrates four key skills embedded in our work: Curiosity, Listening, Imagination, Postive Action.
We work primarily with educators, students, and artists who use the power of personal stories to build community and connection and to bridge divides.
Our new brand guidelines, logos, and fonts are here: https://stylekit.example/lanternfold-9
I've attached a mock-up of the graphic and the required text. (Note the attached design was created by a staff person, your final design does not need to be the same. The color scheme and text of the final design should match the brand guidelines above.)
The graphic will be used for both web and print media and should include the purple Lanternfold 9 logo (also attached).
Ideally the final design will delight audiences and spark interest in our work.

```html
<!DOCTYPE html>
<html lang="en">
<head>
<meta charset="utf-8">
<title>Lanternfold 9 — Four Skills Cycle</title>
<link href="https://fonts.googleapis.com/css2?family=Montserrat:wght@500;600;700&display=swap" rel="stylesheet">
<style>
  :root {
    --curiosity: #e5c947;
    --curiosity-tint: #faf5df;
    --action: #ee4344;
    --action-tint: #fbdde0;
    --imagination: #4cb88b;
    --imagination-tint: #e0f2ea;
    --listening: #f29556;
    --listening-tint: #fce9de;
    --brand-purple: #663399;
    --ink: #1f1f1f;
    --paper: #ffffff;
  }
  html, body {
    margin: 0;
    width: 1200px;
    height: 1200px;
    overflow: hidden;
    background: var(--paper);
  }
  .infographic {
    position: absolute;
    left: 0;
    top: 176px;
    width: 1200px;
    height: 848px;
    display: block;
  }
  .infographic text {
    font-family: "Montserrat", Arial, sans-serif;
  }
  .skill-title { font-size: 36px; font-weight: 700; }
  .skill-body, .link-text { font-size: 22px; font-weight: 500; fill: var(--ink); letter-spacing: 0.6px; }
  .title-curiosity { fill: var(--curiosity); }
  .title-action { fill: var(--action); }
  .title-listening { fill: var(--listening); }
  .title-imagination { fill: var(--imagination); }
  .bracket { fill: none; stroke-width: 6; }
  .bracket-node { fill: var(--paper); stroke-width: 5; }
  .bracket-curiosity { stroke: var(--curiosity); }
  .bracket-action { stroke: var(--action); }
  .bracket-listening { stroke: var(--listening); }
  .bracket-imagination { stroke: var(--imagination); }
  .arrow-curiosity { fill: var(--curiosity); }
  .arrow-action { fill: var(--action); }
  .arrow-imagination { fill: var(--imagination); }
  .arrow-listening { fill: var(--listening); }
  .brand-name { font-size: 28px; font-weight: 600; fill: var(--brand-purple); }
  .brand-dot { fill: var(--brand-purple); }
</style>
</head>
<body>
<svg class="infographic" viewBox="97 350 1741 1230" xmlns="http://www.w3.org/2000/svg" role="img" aria-label="Cycle of four skills: Curiosity, Listening, Imagination and Positive Action">
  <defs>
    <linearGradient id="axis-fade-top" x1="0" y1="0" x2="0" y2="1">
      <stop offset="0" stop-color="#999" stop-opacity="0"/>
      <stop offset="1" stop-color="#777"/>
    </linearGradient>
    <linearGradient id="axis-fade-bottom" x1="0" y1="0" x2="0" y2="1">
      <stop offset="0" stop-color="#777"/>
      <stop offset="1" stop-color="#999" stop-opacity="0"/>
    </linearGradient>
    <filter id="hub-shadow" x="-30%" y="-30%" width="160%" height="160%">
      <feDropShadow dx="4" dy="6" stdDeviation="6" flood-color="#000" flood-opacity="0.35"/>
    </filter>
  </defs>

  <g class="brackets">
    <path class="bracket bracket-curiosity" d="M398,586 Q285,760 278,942 L163,942"/>
    <circle class="bracket-node bracket-curiosity" cx="405" cy="573" r="12"/>
    <path class="bracket bracket-listening" d="M163,1028 L278,1028 Q285,1200 398,1370"/>
    <circle class="bracket-node bracket-listening" cx="405" cy="1383" r="12"/>
    <path class="bracket bracket-action" d="M1542,586 Q1655,760 1662,942 L1773,942"/>
    <circle class="bracket-node bracket-action" cx="1535" cy="573" r="12"/>
    <path class="bracket bracket-imagination" d="M1773,1028 L1662,1028 Q1655,1200 1542,1370"/>
    <circle class="bracket-node bracket-imagination" cx="1535" cy="1383" r="12"/>
  </g>

  <rect x="964" y="655" width="2.5" height="80" fill="url(#axis-fade-top)"/>
  <rect x="964" y="1210" width="2.5" height="90" fill="url(#axis-fade-bottom)"/>

  <g class="cycle">
    <path class="arrow-curiosity" d="M965,728 A225,225 0 0 0 792,965 L770,968 L800,1007 L818,985 L830,965 A140,140 0 0 1 965,830 Z"/>
    <path class="arrow-action" d="M1209,970 A245,245 0 0 0 975,802 L972,786 L930,818 L945,830 A150,150 0 0 1 1150,970 Z"/>
    <path class="arrow-imagination" d="M965,1215 A240,240 0 0 0 1138,980 L1153,978 L1122,932 L1108,958 L1100,990 A150,150 0 0 1 965,1120 Z"/>
    <path class="arrow-listening" d="M720,970 A245,245 0 0 0 960,1140 L960,1168 L1005,1137 L968,1112 A150,150 0 0 1 815,975 L775,970 Z"/>
    <path class="arrow-curiosity" d="M770,968 L800,1007 L818,985 L815,968 Z"/>
  </g>

  <circle cx="965" cy="970" r="149" fill="var(--paper)" filter="url(#hub-shadow)"/>
  <circle class="brand-dot" cx="965" cy="915" r="22"/>
  <text class="brand-name" x="965" y="985" text-anchor="middle">Lanternfold 9</text>

  <rect x="740" y="528" width="456" height="77" fill="var(--action-tint)"/>
  <text class="link-text" x="968" y="561" text-anchor="middle">Your positive action inspires</text>
  <text class="link-text" x="968" y="589" text-anchor="middle">curiosity about what’s possible.</text>

  <rect x="316" y="938" width="369" height="77" fill="var(--curiosity-tint)"/>
  <text class="link-text" x="657" y="969" text-anchor="end">Your curiosity motivates</text>
  <text class="link-text" x="657" y="998" text-anchor="end">you to listen.</text>

  <rect x="1239" y="938" width="368" height="77" fill="var(--imagination-tint)"/>
  <text class="link-text" x="1267" y="969">Your imagination sparks</text>
  <text class="link-text" x="1267" y="998">positive action.</text>

  <rect x="740" y="1337" width="456" height="77" fill="var(--listening-tint)"/>
  <text class="link-text" x="968" y="1370" text-anchor="middle">Your listening lets you take</text>
  <text class="link-text" x="968" y="1399" text-anchor="middle">in new information.</text>

  <text class="skill-title title-curiosity" x="478" y="720" textLength="207" lengthAdjust="spacingAndGlyphs">CURIOSITY</text>
  <text class="skill-body" x="685" y="756" text-anchor="end">Learn from another’s</text>
  <text class="skill-body" x="685" y="785" text-anchor="end">knowledge and experience.</text>

  <text class="skill-title title-action" x="1235" y="720" textLength="338" lengthAdjust="spacingAndGlyphs">POSITIVE ACTION</text>
  <text class="skill-body" x="1237" y="756">Show your words and</text>
  <text class="skill-body" x="1237" y="785">actions matter.</text>

  <text class="skill-title title-listening" x="485" y="1182" textLength="202" lengthAdjust="spacingAndGlyphs">LISTENING</text>
  <text class="skill-body" x="685" y="1214" text-anchor="end">Seek to understand</text>
  <text class="skill-body" x="685" y="1243" text-anchor="end">before speaking.</text>

  <text class="skill-title title-imagination" x="1235" y="1182" textLength="265" lengthAdjust="spacingAndGlyphs">IMAGINATION</text>
  <text class="skill-body" x="1237" y="1214">Consider possibilities</text>
  <text class="skill-body" x="1237" y="1243">beyond what you know.</text>
</svg>
</body>
</html>
```